Medical Device Packaging Project 1 of 5

We are a medical device startup company needing packaging for a total of 5 device brands. This is posting 1 of 5 and the device name is "Vexomira"

Vexomira is an intraocular lens for use in cataract surgery. The target market is Chinese ophthalmologists. The box should be sophisticated and upmarket.

The company name is Tambrel Vision, I have included the logo in the uploaded files section. You should include the logo on the box.

I have uploaded a sample lens boxes from other companies that demonstrate the information needed to be contained on the box in terms of address, warnings, symbols, etc.

I have also uploaded the blank dieline of the boxes

You are welcome and encouraged to also submit to projects 2, 3, 4, and 5 as well. The same rules and expectations apply.

Industry/Entity Type

It Company

Requirements
Should not have
• Should not have any images of an eye or any bionic/futuristic feel to the design
• Note that the quindaret box is for text reference only. You may use the lens image but the futuristic/bionic look is NOT what we are going for with this brand. It should be traditional upmarket medical device artwork.

```html
<!DOCTYPE html>
<html lang="en">
<head>
<meta charset="utf-8">
<title>Vexomira carton dieline</title>
<link rel="stylesheet" href="https://fonts.googleapis.com/css2?family=Ubuntu:wght@400;500&family=Open+Sans:wght@400;600;700&display=swap">
<style>
  :root{
    --sky:#63c0f3;
    --sky-light:#c4e7fb;
    --mid:#2d9be6;
    --deep:#1673d6;
    --navy:#0b4f9c;
    --accent:#1e8ee8;
    --red:#e8333a;
    --white:#ffffff;
    --panel:linear-gradient(160deg,#bfe5fb 0%,#7fcbf5 35%,#3fa6ec 75%,#1d7fe0 100%);
    --strip:linear-gradient(180deg,#7ccaf5 0%,#3ea4ec 100%);
    --flap:linear-gradient(180deg,#4cb3f0 0%,#2a8fe4 100%);
  }
  *{box-sizing:border-box;margin:0;padding:0}
  html,body{width:1000px;height:1200px;overflow:hidden;background:#fff}
  body{font-family:"Open Sans",Arial,sans-serif;position:relative}
  .carton{position:absolute;inset:0}
  .part{position:absolute;overflow:hidden}

  .tab{background:var(--flap)}
  .tab--top-left{left:138px;top:112px;width:118px;height:102px;clip-path:polygon(0 22%,100% 0,100% 100%,0 100%)}
  .tab--top-right{left:768px;top:112px;width:120px;height:102px;clip-path:polygon(0 0,100% 22%,100% 100%,0 100%)}
  .tab--mid-left{left:138px;top:606px;width:118px;height:102px}
  .tab--mid-right{left:768px;top:606px;width:120px;height:102px}
  .tuck--left{left:46px;top:230px;width:72px;height:358px;border-radius:24px 0 0 24px;background:linear-gradient(90deg,#2d97e6,#5cbcf2)}
  .tuck--right{left:908px;top:230px;width:72px;height:358px;border-radius:0 24px 24px 0;background:linear-gradient(90deg,#5cbcf2,#2d97e6)}

  .lid{left:256px;top:90px;width:512px;height:138px;background:linear-gradient(0deg,#1e86e2,#5bbaf2)}
  .front{left:256px;top:228px;width:512px;height:360px;background:var(--panel)}
  .side--left{left:118px;top:228px;width:138px;height:360px;background:linear-gradient(90deg,#3fa6ec,#9bd6f8)}
  .side--right{left:768px;top:228px;width:140px;height:360px;background:linear-gradient(90deg,#9bd6f8,#3fa6ec)}
  .base-strip{left:256px;top:588px;width:512px;height:140px;background:var(--strip)}
  .back{left:256px;top:728px;width:512px;height:360px;background:var(--panel)}
  .bottom-flap{left:260px;top:1088px;width:506px;height:48px;background:linear-gradient(180deg,#1d7fe0,#1565d0)}

  .brand{font-family:"Open Sans",Arial,sans-serif;font-weight:600;color:var(--navy);letter-spacing:.5px;white-space:nowrap;display:flex;align-items:center;gap:6px}
  .brand__dot{width:9px;height:9px;border-radius:50%;background:var(--navy)}
  .wordmark{font-family:"Ubuntu",sans-serif;font-weight:400;color:var(--navy);line-height:1;white-space:nowrap}
  .descriptor{font-family:"Open Sans",Arial,sans-serif;font-weight:700;color:var(--accent);white-space:nowrap}
  .edge-note{color:var(--white);white-space:nowrap}
  .edge-note b{font-weight:700}

  .rotated{position:absolute;left:0;top:0;width:360px;height:138px}
  .side--left .rotated{transform:translate(138px,0) rotate(90deg);transform-origin:0 0}
  .side--right .rotated{transform:translate(0,360px) rotate(-90deg);transform-origin:0 0}
  .rotated .brand{position:absolute;left:26px;top:58px;font-size:14px}
  .rotated .wordmark{position:absolute;left:172px;top:42px;font-size:34px;color:var(--white)}
  .rotated .descriptor{position:absolute;left:172px;top:80px;font-size:5.6px;color:var(--navy)}
  .rotated .edge-note{position:absolute;left:172px;top:89px;font-size:7px;color:var(--navy)}

  .lid__inner{position:absolute;inset:0;transform:rotate(180deg)}
  .lid .brand{position:absolute;left:26px;top:54px;font-size:14px}
  .lid__address{position:absolute;left:200px;top:36px;font-size:9.5px;line-height:14px;color:var(--navy)}
  .lid__address strong{font-weight:700}
  .lid .symbols{position:absolute;left:300px;top:98px}

  .front .brand{position:absolute;left:26px;top:136px;font-size:14px}
  .front .wordmark{position:absolute;left:182px;top:62px;font-size:70px}
  .front .descriptor{position:absolute;left:186px;top:134px;font-size:12px}
  .lens-art{position:absolute;left:176px;top:164px;width:278px;height:132px;border-radius:50%;background:radial-gradient(ellipse at 50% 50%,#f4f6f8 0%,#c6cdd3 35%,rgba(150,162,175,.6) 55%,rgba(150,162,175,0) 70%)}
  .front .claim{position:absolute;left:26px;top:282px;font-size:34px;font-weight:700;color:var(--red);line-height:1}
  .front .edge-note{position:absolute;left:26px;top:322px;font-size:15px}

  .base-strip .brand{position:absolute;left:26px;top:40px;font-size:14px}
  .base-strip .wordmark{position:absolute;left:220px;top:32px;font-size:48px}
  .base-strip .descriptor{position:absolute;left:222px;top:82px;font-size:9.5px;color:var(--navy)}
  .base-strip .edge-note{position:absolute;left:242px;top:96px;font-size:12px}

  .notices{position:absolute;left:22px;top:38px;list-style:none}
  .notice{display:flex;gap:10px;height:37.5px}
  .flag{width:32px;height:19px;flex:none;margin-top:2px}
  .flag--gb{background:#1f3a8a}
  .flag--nl{background:linear-gradient(#c8102e 0 33%,#fff 33% 66%,#21468b 66%)}
  .flag--fr{background:linear-gradient(90deg,#0055a4 0 33%,#fff 33% 66%,#ef4135 66%)}
  .flag--de{background:linear-gradient(#000 0 33%,#dd0000 33% 66%,#ffce00 66%)}
  .flag--gr{background:repeating-linear-gradient(#0d5eaf 0 2.1px,#fff 2.1px 4.2px)}
  .flag--it{background:linear-gradient(90deg,#009246 0 33%,#fff 33% 66%,#ce2b37 66%)}
  .flag--pt{background:linear-gradient(90deg,#006600 0 40%,#ff0000 40%)}
  .flag--es{background:linear-gradient(#aa151b 0 25%,#f1bf00 25% 75%,#aa151b 75%)}
  .notice p{font-size:10px;line-height:11px;color:var(--navy)}
  .back .brand{position:absolute;left:376px;top:62px;font-size:14px}
  .back__ring{position:absolute;left:160px;top:58px;width:190px;height:190px;border-radius:50%;border:2px solid rgba(255,255,255,.35);background:radial-gradient(circle,rgba(255,255,255,.18),rgba(255,255,255,0) 70%)}
  .back .wordmark{position:absolute;left:294px;top:236px;font-size:37px;color:var(--white)}
  .back .descriptor{position:absolute;left:296px;top:274px;font-size:7px;color:var(--navy)}
  .back .edge-note{position:absolute;left:310px;top:286px;font-size:9.5px;color:var(--navy)}
  .back .symbols{position:absolute;left:286px;top:318px}

  .symbols{display:flex;align-items:center;gap:4px}
  .sterile{display:flex;border:2px solid var(--white);color:var(--white);font-weight:700;font-size:10px;line-height:14px;background:var(--navy)}
  .sterile span{padding:0 4px}
  .sterile span+span{border-left:2px solid var(--white)}
</style>
</head>
<body>
<div class="carton">
  <div class="part tab tab--top-left"></div>
  <div class="part tab tab--top-right"></div>
  <div class="part tab tab--mid-left"></div>
  <div class="part tab tab--mid-right"></div>
  <div class="part tuck--left"></div>
  <div class="part tuck--right"></div>

  <section class="part lid">
    <div class="lid__inner">
      <div class="brand"><span class="brand__dot"></span>Tambrel Vision</div>
      <div class="lid__address">
        <strong>Tambrel Vision Limited</strong><br>
        Unit No., Street Name, City Name, Country, Postal Code<br>
        www.tambrelvision.com | info@tambrelvision.com
      </div>
      <div class="symbols">
        <div class="sterile"><span>STERILE</span><span>EO</span></div>
        <svg width="96" height="20" viewBox="0 0 96 20" fill="none" stroke="#fff" stroke-width="1.8">
          <path d="M10 2 L18 18 H2 Z" stroke-linejoin="round"/><line x1="10" y1="8" x2="10" y2="13"/>
          <circle cx="32" cy="10" r="8"/><line x1="26" y1="4" x2="38" y2="16"/>
          <circle cx="54" cy="10" r="8"/><line x1="48" y1="16" x2="60" y2="4"/>
          <circle cx="76" cy="10" r="8"/><path d="M71 12 Q76 5 81 12"/>
        </svg>
      </div>
    </div>
  </section>

  <section class="part side--left">
    <div class="rotated">
      <div class="brand"><span class="brand__dot"></span>Tambrel Vision</div>
      <div class="wordmark">Vexomira</div>
      <div class="descriptor">HYDROPHOBIC ACRYLIC INTRAOCULAR LENS</div>
      <div class="edge-note"><b>Aspheric</b> with <b>360°</b> square edge</div>
    </div>
  </section>

  <section class="part front">
    <div class="brand"><span class="brand__dot"></span>Tambrel Vision</div>
    <div class="wordmark">Vexomira</div>
    <div class="descriptor">HYDROPHOBIC ACRYLIC INTRAOCULAR LENS</div>
    <div class="lens-art" role="img" aria-label="Intraocular lens with two curved haptics"></div>
    <div class="claim">Aspheric</div>
    <div class="edge-note">With <b>360°</b> square edge</div>
  </section>

  <section class="part side--right">
    <div class="rotated">
      <div class="brand"><span class="brand__dot"></span>Tambrel Vision</div>
      <div class="wordmark">Vexomira</div>
      <div class="descriptor">HYDROPHOBIC ACRYLIC INTRAOCULAR LENS</div>
      <div class="edge-note"><b>Aspheric</b> with <b>360°</b> square edge</div>
    </div>
  </section>

  <section class="part base-strip">
    <div class="brand"><span class="brand__dot"></span>Tambrel Vision</div>
    <div class="wordmark">Vexomira</div>
    <div class="descriptor">HYDROPHOBIC ACRYLIC INTRAOCULAR LENS</div>
    <div class="edge-note"><b>Aspheric</b> with <b>360°</b> square edge</div>
  </section>

  <section class="part back">
    <div class="back__ring"></div>
    <ul class="notices">
      <li class="notice"><span class="flag flag--gb" role="img" aria-label="English"></span><p>Contains one sterile intraocular lens<br>Do not use if the packaging is damaged<br>Do not resterilize</p></li>
      <li class="notice"><span class="flag flag--nl" role="img" aria-label="Dutch"></span><p>Bevat één steriele intraoculaire lens<br>Niet gebruiken als de verpakking beschadigd is<br>Niet opnieuw steriliseren</p></li>
      <li class="notice"><span class="flag flag--fr" role="img" aria-label="French"></span><p>Contient une lentille intraoculaire stérile<br>Ne pas utiliser si l’emballage est endommagé<br>Ne pas restériliser</p></li>
      <li class="notice"><span class="flag flag--de" role="img" aria-label="German"></span><p>Enthält eine sterile intraokulare Linse<br>Nicht verwenden, wenn die Verpackung beschädigt ist<br>Nicht resterilisieren</p></li>
      <li class="notice"><span class="flag flag--gr" role="img" aria-label="Greek"></span><p>Περιέχει ένα αποστειρωμένο ενδοφθάλμια φακό<br>Μην το χρησιμοποιείτε εάν η συσκευασία έχει υποστεί ζημιά<br>Μην επαναποστειρώνετε</p></li>
      <li class="notice"><span class="flag flag--it" role="img" aria-label="Italian"></span><p>Contiene una lente intraoculare sterile<br>Non usare se la confezione è danneggiata<br>Non risterilizzare</p></li>
      <li class="notice"><span class="flag flag--pt" role="img" aria-label="Portuguese"></span><p>Contém uma lente intra-ocular esterilizada<br>Não use se a embalagem está danificada<br>Não reesterilize</p></li>
      <li class="notice"><span class="flag flag--es" role="img" aria-label="Spanish"></span><p>Contiene una lente intraocular estéril<br>No utilizar si el envase está dañado<br>No vuelva a esterilizar</p></li>
    </ul>
    <div class="brand"><span class="brand__dot"></span>Tambrel Vision</div>
    <div class="wordmark">Vexomira</div>
    <div class="descriptor">HYDROPHOBIC ACRYLIC INTRAOCULAR LENS</div>
    <div class="edge-note"><b>Aspheric</b> with <b>360°</b> square edge</div>
    <div class="symbols">
      <div class="sterile"><span>STERILE</span><span>EO</span></div>
      <svg width="96" height="20" viewBox="0 0 96 20" fill="none" stroke="#fff" stroke-width="1.8">
        <path d="M10 2 L18 18 H2 Z" stroke-linejoin="round"/><line x1="10" y1="8" x2="10" y2="13"/>
        <circle cx="32" cy="10" r="8"/><line x1="26" y1="4" x2="38" y2="16"/>
        <circle cx="54" cy="10" r="8"/><line x1="48" y1="16" x2="60" y2="4"/>
        <circle cx="76" cy="10" r="8"/><path d="M71 12 Q76 5 81 12"/>
      </svg>
    </div>
  </section>

  <div class="part bottom-flap"></div>
</div>
</body>
</html>
```